Luxury and organic beauty products need a Design

We need a bottle and packaging design for a new business in New Zealand, called Keravi Botanicals. We are creating a selection of Luxury and premium products to have at the Keravi luxury villa's (www.keraviluxuryvilla.com), as well to sell online and at boutique stores.

The products are: Body wash, Shampoo, Conditioner, Hand wash, Body lotion, Air fresheners and Bath salts.

We would like to use the Keravi Botanicals logo in Silver as Keravi Luxury Villa's a having it in Gold, so it separates the two products. Also the packaging will be Navy Blue along with the silver.

The final design should be sleek, sophisticated and have a luxury feel. Our customers will have the product in the bathroom and kitchen so the bottles must be proud to show off. " This should look and feel like a very high end product.

Boxes will have embossed writing (logo) and a slightly textured feel or look.

Please find attached images of some examples to use for inspiration only.

Target Market(s)

Luxury boutique villas, Boutique stores, High end stores

Industry/Entity Type

Personal and hair care

Colors
0054AA
0677BA
7BADD7
CADEEF
E8F1F8
FFC000
F8CF3A
FAE287
FDF2CF
FEFAEE

Requirements
Must have
• Use the provided Logo, look and feel luxurious, but at the same time organic
Nice to have
• A bottle that reminds precious stones. I have just attached an example
Should not have
• Dark colour, heavy fonts

```html
<!DOCTYPE html>
<html lang="en">
<head>
<meta charset="utf-8">
<title>Keravi Botanicals — Packaging Range</title>
<link href="https://fonts.googleapis.com/css2?family=Jost:wght@400&family=Kaushan+Script&display=swap" rel="stylesheet">
<style>
  :root {
    --ground: #f1efea;
    --label: #050505;
    --silver: #cfcfd2;
    --leaf-light: #eef0e6;
    --leaf-mid: #b9c6a6;
    --leaf-deep: #6f8a5e;
    --bottle: #e9e3e6;
    --bottle-shade: #d9d1d5;
    --cap: #fbfbfb;
    --cap-edge: #dedede;
  }
  * { box-sizing: border-box; margin: 0; padding: 0; }
  html, body { width: 1200px; height: 960px; overflow: hidden; }
  body { background: var(--ground); position: relative; font-family: "Jost", sans-serif; }

  .pack {
    position: absolute;
    background: radial-gradient(circle at 35% 30%, var(--leaf-light) 0%, var(--leaf-mid) 55%, var(--leaf-deep) 130%);
    box-shadow: 0 2px 6px rgba(0,0,0,0.08);
  }
  .pack--shampoo { left: 110px; top: 215px; width: 284px; height: 535px; }
  .pack--conditioner { left: 506px; top: 215px; width: 283px; height: 535px; }
  .pack--salt { left: 818px; top: 464px; width: 264px; height: 266px; }

  .label {
    position: absolute;
    background: var(--label);
    color: var(--silver);
    display: flex; flex-direction: column; align-items: center;
    text-align: center;
  }
  .pack--shampoo .label, .pack--conditioner .label { left: 49px; top: 131px; width: 185px; height: 202px; padding-top: 22px; }
  .pack--salt .label { left: 41px; top: 57px; width: 202px; height: 158px; padding-top: 14px; }

  .brand-mark { width: 40px; height: 40px; border: 2px solid var(--silver); border-radius: 50%; }
  .brand-name { font-weight: 400; font-size: 19px; letter-spacing: 1.5px; line-height: 1.1; margin-top: 10px; }
  .brand-name small { display: block; font-size: 9px; letter-spacing: 2.5px; margin-top: 2px; }
  .product { font-family: "Kaushan Script", cursive; font-size: 31px; margin-top: 14px; line-height: 1; }
  .size { font-size: 9px; letter-spacing: 2px; margin-top: 14px; }

  .pack--salt .brand-mark { width: 36px; height: 36px; }
  .pack--salt .product { font-size: 20px; margin-top: 10px; }
  .pack--salt .size { margin-top: 4px; }

  .bottle { position: absolute; left: 372px; top: 195px; width: 112px; height: 565px; }
  .bottle .label { left: 18px; top: 353px; width: 81px; height: 153px; padding-top: 12px; }
  .bottle .brand-mark { width: 26px; height: 26px; border-width: 1.5px; }
  .bottle .brand-name { font-size: 11px; letter-spacing: 0.8px; margin-top: 6px; }
  .bottle .brand-name small { font-size: 5px; letter-spacing: 1.2px; }
  .bottle .product { font-size: 17px; margin-top: 9px; }
  .bottle .size { font-size: 5px; margin-top: 6px; }
</style>
</head>
<body>
  <div class="pack pack--shampoo" role="img" aria-label="Botanical watercolour pattern of clover leaves and small yellow flowers">
    <div class="label">
      <div class="brand-mark"></div>
      <div class="brand-name">KERAVI<small>BOTANICALS</small></div>
      <div class="product">Shampoo</div>
      <div class="size">100 ML</div>
    </div>
  </div>

  <div class="pack pack--conditioner" role="img" aria-label="Botanical watercolour pattern of clover leaves and small yellow flowers">
    <div class="label">
      <div class="brand-mark"></div>
      <div class="brand-name">KERAVI<small>BOTANICALS</small></div>
      <div class="product">Conditioner</div>
      <div class="size">100 ML</div>
    </div>
  </div>

  <div class="pack pack--salt" role="img" aria-label="Botanical watercolour pattern of clover leaves and small yellow flowers">
    <div class="label">
      <div class="brand-mark"></div>
      <div class="brand-name">KERAVI<small>BOTANICALS</small></div>
      <div class="product">Bath Salt</div>
      <div class="size">150 GRAMS</div>
    </div>
  </div>

  <div class="bottle">
    <svg width="112" height="565" viewBox="0 0 112 565">
      <path d="M26 64 Q26 84 12 100 Q4 110 4 128 L4 548 Q4 562 18 562 L94 562 Q108 562 108 548 L108 128 Q108 110 100 100 Q86 84 86 64 Z" fill="var(--bottle)"/>
      <rect x="4" y="520" width="104" height="42" rx="12" fill="var(--bottle-shade)" opacity="0.6"/>
      <rect x="24" y="0" width="64" height="66" rx="5" fill="var(--cap)" stroke="var(--cap-edge)"/>
    </svg>
    <div class="label">
      <div class="brand-mark"></div>
      <div class="brand-name">KERAVI<small>BOTANICALS</small></div>
      <div class="product">Shampoo</div>
      <div class="size">100 ML</div>
    </div>
  </div>
</body>
</html>
```